Constructor Company /Carpenter

We need a high quality design for a Brochure up to 8pages.Copmany does plastering, building houses, make renovation of houses.
Updates

Ich brauche zusätzliche Tage um durchzusehen

Target Market(s)

The Brochure is a high quality hand out for architects.

Industry/Entity Type

Construction Company

Font styles to use
Sans Serif

Colors

Designer to choose colors to be used in the design.

Requirements
Must have
• You can build the brochure like the website www.qelvorix.ch is built. The brochure needs to look clean, modern and professionell.
• The brochure need to have the same colors like website www.qelvorix.ch

```html
<!DOCTYPE html>
<html lang="en">
<head>
<meta charset="utf-8">
<title>Qelvorix Bau GmbH – Brochure Spreads</title>
<link href="https://fonts.googleapis.com/css2?family=Montserrat:wght@500;700;800;900&family=Open+Sans:wght@400;600;700&display=swap" rel="stylesheet">
<style>
:root{
  --blue:#1a4fa0;
  --blue-dark:#143d7d;
  --ink:#222326;
  --band:#2b2b2d;
  --text:#4a4a4e;
  --muted:#7a7a80;
  --paper:#ffffff;
  --stage:#8e8e90;
  --rule:#d6d8de;
}
*{margin:0;padding:0;box-sizing:border-box}
html,body{width:1200px;height:1200px;overflow:hidden;background:var(--stage)}
body{position:relative;font-family:"Open Sans",Arial,sans-serif;color:var(--text)}
.spread{position:absolute;left:50px;width:1100px;height:255px;background:var(--paper);overflow:hidden;box-shadow:0 6px 16px rgba(0,0,0,.25)}
.spread::after{content:"";position:absolute;left:549px;top:0;width:2px;height:100%;background:linear-gradient(90deg,rgba(0,0,0,.06),rgba(0,0,0,0))}
.s1{top:25px}.s2{top:310px}.s3{top:595px}.s4{top:880px}
.abs{position:absolute}
.photo{position:absolute}
.wordmark{font-family:"Montserrat",Arial,sans-serif;font-weight:500;font-size:19px;letter-spacing:-.3px;display:flex;align-items:center;gap:7px}
.wordmark .sq{width:12px;height:12px;background:currentColor;display:inline-block}
.blue-bar{position:absolute;background:var(--blue)}
h2,h3,.head{font-family:"Montserrat",Arial,sans-serif;font-weight:900;color:var(--ink);text-transform:uppercase}
.kicker{color:var(--blue)}
p{font-size:6.4px;line-height:1.45}
ul{list-style:none;font-size:6px;line-height:1.4}
.lbl{font-weight:700;font-size:6.2px;color:var(--ink);margin-top:5px}

/* spread 1 */
.s1 .band{left:0;top:0;width:550px;height:115px;background:var(--band)}
.s1 .wordmark.light{left:40px;top:40px;color:#fff}
.contact{left:390px;top:20px;width:135px;text-align:right;color:#fff;font-size:6px;line-height:1.4}
.contact .head{color:#fff;font-size:8.5px;font-weight:800;margin-bottom:2px}
.s1 .hero-interior{left:45px;top:72px;width:340px;height:165px;background:linear-gradient(135deg,#f3c27c,#b8682a 55%,#6a3515);border:3px solid #fff}
.s1 .wordmark.dark{right:40px;top:26px;color:var(--ink)}
.s1 .url{right:40px;top:50px;font-size:7px;font-weight:700;color:var(--ink)}
.s1 .hero-villa{left:555px;top:68px;width:450px;height:105px;background:linear-gradient(180deg,#a9cdea 0%,#f1ede4 45%,#5d8a3b 70%,#2fa3d4 100%)}
.s1 .tagline{left:580px;top:190px}
.s1 .tagline .kicker{font-family:"Montserrat",sans-serif;font-weight:700;font-size:13px}
.s1 .tagline .head{font-size:13px}

/* spread 2 */
.s2 .living{left:0;top:0;width:300px;height:255px;background:linear-gradient(160deg,#8fb36f 0%,#d9dcdc 35%,#6f7072 75%,#3b3b3d)}
.s2 .small-a{left:308px;top:14px;width:200px;height:108px;background:linear-gradient(135deg,#c9c4b8,#8e8779 60%,#e0d9cc)}
.s2 .small-b{left:308px;top:132px;width:200px;height:108px;background:linear-gradient(135deg,#e7ddc9,#9a5b34 55%,#c79b68)}
.toc{left:640px;top:28px;width:330px}
.toc h2{font-size:13px;letter-spacing:.3px;margin-bottom:12px}
.toc li{display:flex;justify-content:space-between;font-size:7px;line-height:15.5px;color:var(--text)}
.toc li b{color:var(--ink)}
.s2 .accent{left:885px;top:0;width:5px;height:18px}
.s2 .foot{left:640px;top:238px;width:260px;height:3px}

/* spread 3 */
.svc{position:absolute;width:225px}
.svc h3{font-size:7.6px;line-height:1.2;margin-bottom:4px}
.svc h3 .kicker{display:block}
.svc .uline{width:40px;height:2px;background:var(--blue);margin-bottom:4px}
.svc p{font-size:5.6px;line-height:1.38}
.svc ul{font-size:5.4px;line-height:1.3}
.svc .lbl{font-size:5.6px;margin-top:3px;margin-bottom:1px}
.cols{display:flex;gap:14px}
.s3 .divider-v{left:278px;top:18px;width:0;height:222px;border-left:1px dashed var(--rule)}
.s3 .divider-h{left:30px;top:132px;width:495px;height:0;border-top:1px dashed var(--rule)}
.s3 .house{left:775px;top:0;width:325px;height:255px;background:linear-gradient(180deg,#3f8fd8 0%,#b7d3ea 30%,#a7856c 55%,#4f8a36 100%)}

/* spread 4 */
.about{left:30px;top:24px;width:300px}
.about h2{font-size:15px;margin-bottom:8px}
.about p{font-size:5.8px;line-height:1.4;margin-bottom:3px}
.values{left:22px;top:160px;width:320px;display:flex;justify-content:space-between}
.value{width:100px;text-align:center}
.value svg{display:block;margin:0 auto 4px}
.value .head{color:var(--blue);font-size:6.6px;font-weight:800;line-height:1.2}
.value p{font-size:5.8px;font-weight:600;color:var(--ink);line-height:1.3;margin-top:2px}
.s4 .bedroom{left:355px;top:10px;width:400px;height:245px;background:linear-gradient(160deg,#d8d8d8,#8e8e90 50%,#5a4030 85%,#bfbcb8)}
.team{left:775px;top:18px;width:310px}
.team h2{font-size:13px}
.team .uline{width:55px;height:2px;background:var(--blue);margin:4px 0 8px}
.member{display:flex;gap:10px;height:50px;align-items:flex-start}
.member .portrait{width:44px;height:44px;background:linear-gradient(180deg,#c9cdd3,#f4f4f4)}
.member .name{font-family:"Montserrat",sans-serif;font-weight:900;font-size:12px;color:var(--blue);line-height:1.2}
.member ul{font-size:5.4px;color:var(--text);line-height:1.3}
.member li::before{content:"✓ ";color:var(--blue)}
.s4 .foot-l{left:25px;top:247px;width:300px;height:3px}
.s4 .foot-r{left:770px;top:247px;width:310px;height:3px}
.s4 .top-r{left:840px;top:0;width:260px;height:3px}
</style>
</head>
<body>

<!-- Spread 1: back and front cover -->
<section class="spread s1">
  <div class="abs band"></div>
  <div class="abs wordmark light"><span class="sq"></span>Qelvorix Bau GmbH</div>
  <div class="abs contact">
    <div class="head">Get in touch</div>
    <div>info@qelvorix.ch</div>
    <div>079 418 26 70</div>
    <div>Qelvorix Bau GmbH, Lindenweg 8</div>
    <div>4147 Aesch</div>
  </div>
  <div class="photo hero-interior" role="img" aria-label="Photo of a warm wood-toned open kitchen and living room"></div>
  <div class="blue-bar" style="left:45px;top:246px;width:340px;height:4px"></div>

  <div class="abs wordmark dark"><span class="sq"></span>Qelvorix Bau GmbH</div>
  <div class="abs url">⊕ www.qelvorix.ch</div>
  <div class="photo hero-villa" role="img" aria-label="Photo of a white villa with palm trees and a pool"></div>
  <div class="blue-bar" style="left:1086px;top:212px;width:5px;height:26px"></div>
  <div class="abs tagline">
    <div class="kicker">YOUR PLASTERER FROM</div>
    <div class="head">Aesch in Basel and surroundings</div>
  </div>
</section>

<!-- Spread 2: gallery and table of content -->
<section class="spread s2">
  <div class="photo living" role="img" aria-label="Photo of a bright modern living room with white sofas"></div>
  <div class="photo small-a" role="img" aria-label="Photo of a living room with grey plastered wall"></div>
  <div class="photo small-b" role="img" aria-label="Photo of a classic furnished living room with fireplace"></div>
  <div class="blue-bar accent"></div>
  <div class="abs toc">
    <h2>Table of content</h2>
    <ul>
      <li><span>About <b>Our Company</b></span><b>2</b></li>
      <li><span>Our <b>History</b></span><b>3</b></li>
      <li><span>How <b>We Create</b></span><b>3</b></li>
      <li><span>Our <b>Services &amp; Why you should Choose us</b></span><b>4</b></li>
      <li><span>Meet <b>Our Team</b></span><b>5</b></li>
      <li><span>Facades</span><b>6</b></li>
      <li><span>Plaster</span><b>6</b></li>
      <li><span>To Paint</span><b>7</b></li>
      <li><span>Modification</span><b>7</b></li>
      <li><span>Gardening</span><b>7</b></li>
      <li><span>Testimonials</span><b>8</b></li>
    </ul>
  </div>
  <div class="blue-bar foot"></div>
</section>

<!-- Spread 3: services -->
<section class="spread s3">
  <div class="abs divider-v"></div>
  <div class="abs divider-h"></div>

  <article class="svc" style="left:35px;top:20px">
    <h3><span class="kicker">Facades in Basel,</span>Basel-Land and Aargau</h3>
    <div class="uline"></div>
    <p>We are your specialists for your wishes in the field of plasters and renovations. Our many years of professional experience makes us a specialist for your plaster work indoors and outdoors.</p>
    <div class="cols">
      <div><div class="lbl">We offer the following services:</div>
        <ul><li>Fassadenputze</li><li>Basement insulation</li><li>Ceiling insulation</li><li>Perimeter insulation</li></ul></div>
      <div><div class="lbl">You benefit from:</div>
        <ul><li>Heat protection</li><li>Energy saving</li><li>Soundproofing</li><li>Fire protection</li><li>Nice aesthetics</li></ul></div>
    </div>
  </article>

  <article class="svc" style="left:292px;top:20px">
    <h3><span class="kicker">Plastering in Basel,</span>Basel-Land and Aargau</h3>
    <div class="uline"></div>
    <p>We are your specialists for your wishes in the field of plasters and renovations. Our many years of professional experience makes us a specialist for your plaster work indoors and outdoors.</p>
    <div class="lbl">We offer the following services:</div>
    <div class="cols">
      <ul><li>Gipserarbeiten</li><li>Renovations</li><li>Insulations</li><li>Clay plasters</li><li>Isolations</li></ul>
      <ul><li>Altbausanierungen</li><li>Renovating facades</li><li>Mineral abrasions</li><li>Basic plasters</li><li>Fillings</li></ul>
      <ul><li>Special plasters</li><li>Drywall</li><li>Kittfugen</li></ul>
    </div>
  </article>

  <article class="svc" style="left:35px;top:140px">
    <h3><span class="kicker">Rebuilding in Basel,</span>Basel-Land and Aargau</h3>
    <div class="uline"></div>
    <p>Expertly, we do all the reconstruction work for you. Renovations and renovations have been our specialty for years.</p>
    <div class="lbl">We advise you individually and realize your wishes.</div>
    <div class="lbl">We offer the following alterations:</div>
    <div class="cols">
      <ul><li>Renovation renovation</li><li>Bathroom and kitchen</li><li>Wall demolition</li></ul>
      <ul><li>Wall catchment</li><li>Spitz work</li></ul>
    </div>
  </article>

  <article class="svc" style="left:292px;top:140px">
    <h3><span class="kicker">Gardening in Basel,</span>Basel-Land and Aargau</h3>
    <div class="uline"></div>
    <p>Our private customers appreciate our additional experience in the environment work very much. Therefore, we realize your dreams in your garden.</p>
    <div class="lbl">We are happy to do the following gardening for you:</div>
    <div class="cols">
      <ul><li>Horticulture</li><li>Gartenunterhalt</li><li>Landscaping</li><li>Terrace greenery</li></ul>
      <ul><li>Garden wall</li><li>Decking</li><li>Herbal Schneck</li><li>Seating</li></ul>
      <ul><li>Canopy</li><li>Privacy</li><li>Rockery</li><li>Garden stairs</li></ul>
    </div>
  </article>

  <article class="svc" style="left:568px;top:20px;width:195px">
    <h3><span class="kicker">Plastering in Basel,</span>Basel-Land and Aargau</h3>
    <div class="uline"></div>
    <p>We are your specialists for your wishes in the field of plasters and renovations. Our many years of professional experience makes us a specialist for your plaster work indoors and outdoors.</p>
    <div class="lbl">We offer the following exterior work:</div>
    <ul><li>Cleaning</li><li>Repainting</li><li>Special colors</li><li>Mold removal</li><li>Coating against mold</li></ul>
    <p style="margin-top:8px">We are your specialists for your wishes in the field of plasters and renovations. Our many years of professional experience makes us a specialist for your plaster work indoors and outdoors.</p>
    <div class="lbl">We offer the following interior work:</div>
    <ul><li>Painting work</li><li>Wallpapering</li><li>Special colors</li><li>Mold removal</li><li>Coating against mold</li></ul>
  </article>

  <div class="photo house" role="img" aria-label="Photo of a stone family house with lawn under a blue sky"></div>
</section>

<!-- Spread 4: about us and team -->
<section class="spread s4">
  <div class="blue-bar top-r"></div>
  <div class="abs about">
    <h2>About us</h2>
    <p>Our passion is to create and change things that make people happy.</p>
    <p>Whether the conversion of your house, the renovation of a charming apartment or new freshness in your garden – we are your partner when it comes to craftsmanship and quality work.</p>
    <p>Years of experience and networked thinking make us your efficient partner which realizes your construction project cost-consciously. We do work with professional pride and attention to detail.</p>
    <p>Our clients benefit from the extensive experience we have gained over the last decades in various construction sectors.</p>
    <p>Over the years, we have gained experience in the areas of renovation, remodeling, facades, insulation, dry and wet construction and much more.</p>
    <p>We have some references for you on our website. Of course, we look forward to hearing from you so we can convince you immediately.</p>
  </div>

  <div class="abs values">
    <div class="value">
      <svg width="28" height="28" viewBox="0 0 30 30"><circle cx="15" cy="15" r="14" fill="var(--blue)"/><circle cx="15" cy="12" r="4.5" fill="none" stroke="#fff" stroke-width="1.8"/><path d="M8 23c1.5-4 4-5.5 7-5.5s5.5 1.5 7 5.5" fill="none" stroke="#fff" stroke-width="1.8"/></svg>
      <div class="head">Personal advice</div>
      <p>We take time for your concerns.</p>
    </div>
    <div class="value">
      <svg width="28" height="28" viewBox="0 0 30 30"><circle cx="15" cy="15" r="14" fill="var(--blue)"/><path d="M15 7c3 4.5 5 7.5 5 10a5 5 0 0 1-10 0c0-2.5 2-5.5 5-10z" fill="#fff"/></svg>
      <div class="head">Environmentally friendly</div>
      <p>We pay attention to the environment and are economical.</p>
    </div>
    <div class="value">
      <svg width="28" height="28" viewBox="0 0 30 30"><circle cx="15" cy="15" r="14" fill="var(--blue)"/><circle cx="15" cy="15" r="8" fill="none" stroke="#fff" stroke-width="1.8"/><path d="M15 10v5l3.5 2.5" fill="none" stroke="#fff" stroke-width="1.8" stroke-linecap="round"/></svg>
      <div class="head">Years of experience</div>
      <p>We save your time through our experience.</p>
    </div>
  </div>
  <div class="blue-bar foot-l"></div>

  <div class="photo bedroom" role="img" aria-label="Photo of a bedroom with grey patterned wallpaper, chandelier and white bed"></div>

  <div class="abs team">
    <h2>Meet our team</h2>
    <div class="uline"></div>
    <div class="member">
      <div class="portrait" role="img" aria-label="Portrait photo of team member"></div>
      <div><div class="name">Arben Krasniqi</div>
        <ul><li>Founder and master plasterer</li><li>Over twenty years on site</li><li>Facades and insulation</li><li>Your first contact person</li></ul></div>
    </div>
    <div class="member">
      <div class="portrait" role="img" aria-label="Portrait photo of team member"></div>
      <div><div class="name">QB Mitarbeiter</div>
        <ul><li>Interior plaster specialist</li><li>Drywall and fillings</li><li>Clean and precise work</li><li>Part of the team since 2012</li></ul></div>
    </div>
    <div class="member">
      <div class="portrait" role="img" aria-label="Portrait photo of team member"></div>
      <div><div class="name">QB Mitarbeiter</div>
        <ul><li>Painting and special colors</li><li>Mold removal and coating</li><li>Renovation of old buildings</li><li>Careful with every detail</li></ul></div>
    </div>
    <div class="member">
      <div class="portrait" role="img" aria-label="Portrait photo of team member"></div>
      <div><div class="name">Driton Berisha</div>
        <ul><li>Project lead for rebuilding</li><li>Bathroom and kitchen work</li><li>Gardening and landscaping</li><li>Plans each site with you</li></ul></div>
    </div>
  </div>
  <div class="blue-bar foot-r"></div>
</section>

</body>
</html>
```